Two flyers with cover pages for business services company

We need to create two double sided A4 flyers for our company. We are a company that provides professional services for businesses in Dubai, UAE.
Please note that there are two different flyers. The design must be identical. Each has a cover page. The cover page will be duplicated for both flyers.
Please note that we have added images of the Dubai skyline, clip art as place-hold/temporary images. These can be changed to be more fitting to your design. We prefer to have free images where possible but are open to purchasing Pixelorra images if required.
We have recommended a colour palet below. You are welcome to change some colours to be more fitting to the design. However, we must have black, white and blue and per the logo.
Target Market(s)
Businesses, entrepreneurs, professionals
Industry/Entity Type
Business Service
Requirements
Must have
- The cover page should be less crowded and more visual. So mostly images with our logo and tagline.

```html
<!DOCTYPE html>
<html lang="en">
<head>
<meta charset="utf-8">
<title>Nexora Flyers</title>
<link rel="stylesheet" href="https://fonts.googleapis.com/css2?family=Montserrat:wght@400;600;700;800&family=PT+Sans:ital,wght@0,400;0,700;1,400&display=swap">
<style>
  :root {
    --navy: #1c3766;
    --blue: #1a5cae;
    --deep: #19345e;
    --orange: #f4901e;
    --white: #ffffff;
    --ink: #1e1e1e;
    --stage: #e9e9ea;
  }
  * { box-sizing: border-box; margin: 0; padding: 0; }
  html, body { width: 1200px; height: 1200px; overflow: hidden; background: var(--stage); }
  .canvas { position: relative; width: 1200px; height: 1200px; }

  .flyer { position: absolute; background: var(--white); overflow: hidden; box-shadow: 0 4px 14px rgba(0,0,0,.18); }
  .flyer--inside { left: 27px; top: 74px; width: 587px; height: 828px; }
  .flyer--cover { left: 626px; top: 249px; width: 560px; height: 792px; }

  .hero-photo { position: absolute; left: 0; top: 0; width: 100%; height: 350px;
    background: linear-gradient(180deg, #9cc7ea 0%, #c9e1f4 55%, #ffffff 100%); }
  .headline { position: absolute; left: 0; top: 283px; width: 100%; text-align: center;
    font-family: "Montserrat", sans-serif; font-weight: 800; font-size: 29px; line-height: 33px;
    color: var(--navy); letter-spacing: -0.3px; }

  .stat-tag { position: absolute; left: 34px; height: 23px; background: var(--orange); color: var(--white);
    font-family: "PT Sans", sans-serif; font-size: 15.5px; line-height: 23px; padding-left: 4px; }
  .stat-tag--one { top: 392px; width: 221px; }
  .stat-tag--two { top: 420px; width: 414px; }

  .help-title { position: absolute; left: 37px; top: 469px; font-family: "Montserrat", sans-serif;
    font-weight: 700; font-size: 19.5px; color: var(--ink); letter-spacing: -0.4px; }
  .help-list { position: absolute; left: 36px; top: 500px; list-style: none;
    font-family: "PT Sans", sans-serif; font-size: 11.8px; color: var(--ink); }
  .help-list li { height: 17.4px; line-height: 17.4px; display: flex; align-items: center; }
  .help-list svg { width: 11px; height: 10px; margin-right: 6px; flex: none; }

  .guarantee-tail { position: absolute; left: 536px; top: 487px; width: 51px; height: 117px; background: var(--deep); }
  .guarantee-fold { position: absolute; left: 512px; top: 590px; }
  .guarantee { position: absolute; left: 371px; top: 475px; width: 165px; height: 116px; background: var(--blue);
    padding: 6px; }
  .guarantee-inner { width: 100%; height: 100%; border: 1.5px solid var(--white); color: var(--white);
    text-align: center; font-family: "Montserrat", sans-serif; font-weight: 700; padding-top: 9px; }
  .guarantee-big { font-size: 25px; line-height: 25px; }
  .guarantee-mid { font-size: 16.5px; line-height: 18px; letter-spacing: -0.5px; }
  .guarantee-small { font-size: 10.5px; line-height: 14px; letter-spacing: -0.3px; }

  .director-photo { position: absolute; left: 50px; top: 632px; width: 91px; height: 91px;
    background: linear-gradient(180deg, #f1e7df 0%, #b89883 55%, #2c3344 100%); }
  .director-name { position: absolute; left: 145px; top: 666px; font-family: "PT Sans", sans-serif;
    font-size: 17px; color: var(--blue); }
  .director-role { position: absolute; left: 146px; top: 687px; font-family: "PT Sans", sans-serif;
    font-style: italic; font-size: 8.5px; color: var(--ink); }

  .contact { position: absolute; left: 262px; top: 637px; width: 282px; text-align: center; color: var(--ink); }
  .contact-call { font-family: "Montserrat", sans-serif; font-size: 11.5px; letter-spacing: -0.3px; }
  .contact-call strong { font-weight: 700; }
  .contact-phone { font-family: "PT Sans", sans-serif; font-weight: 700; font-size: 30px; line-height: 30px;
    color: var(--blue); margin-top: 2px; }
  .contact-address { font-family: "Montserrat", sans-serif; font-size: 7.5px; line-height: 9.5px; }
  .contact-web { font-family: "Montserrat", sans-serif; font-size: 18px; letter-spacing: 4px; margin-top: 2px; }

  .footer-rule { position: absolute; left: 0; width: 100%; height: 3px; background: var(--ink); }
  .footer-band { position: absolute; left: 0; width: 100%; background: var(--orange); }

  .brand { position: absolute; display: flex; align-items: center; }
  .brand-dot { width: 36px; height: 36px; border-radius: 50%; background: var(--blue); margin-right: 10px; }
  .brand-name { font-family: "Montserrat", sans-serif; font-weight: 400; font-size: 28px; color: var(--white); letter-spacing: 1px; }
  .brand-since { position: absolute; left: 107px; top: 51px; font-family: "Montserrat", sans-serif;
    font-weight: 700; font-size: 12px; color: var(--white); }

  .revenue { position: absolute; left: 280px; top: 34px; width: 244px; text-align: center;
    font-family: "PT Sans", sans-serif; color: var(--white); font-size: 16.5px; line-height: 19px; }

  .skyline-photo { position: absolute; left: 0; top: 0; width: 100%; height: 702px;
    background: linear-gradient(180deg, #241f6b 0%, #2f3190 40%, #6c5aa8 68%, #b86f95 78%, #2a2448 90%, #1a1a2c 100%); }
  .tagline { position: absolute; left: 248px; top: 18px; width: 290px; text-align: center;
    font-family: "Montserrat", sans-serif; font-weight: 700; font-size: 29px; line-height: 31px;
    color: var(--white); letter-spacing: -1px; }
</style>
</head>
<body>
<main class="canvas">

  <section class="flyer flyer--inside">
    <div class="hero-photo" role="img" aria-label="Two business people in suits shaking hands before a glass office tower and bright sky"></div>
    <h1 class="headline">GROW YOUR BUSINESS THROUGH<br>OUR EXTENSIVE NETWORK</h1>

    <div class="stat-tag stat-tag--one">3000+ Business Connections</div>
    <div class="stat-tag stat-tag--two">570+ Decision Makers, MDs, CEO’s, Head of Purchasing</div>

    <h2 class="help-title">HOW WE CAN HELP YOU</h2>
    <ul class="help-list">
      <li><svg viewBox="0 0 11 10"><path d="M0 0 L6 5 L0 10 Z M5 0 L11 5 L5 10 Z" fill="#4d86c9"/></svg>Reduce your sales cycle time</li>
      <li><svg viewBox="0 0 11 10"><path d="M0 0 L6 5 L0 10 Z M5 0 L11 5 L5 10 Z" fill="#4d86c9"/></svg>Book appointments directly and by pass the gate keeper</li>
      <li><svg viewBox="0 0 11 10"><path d="M0 0 L6 5 L0 10 Z M5 0 L11 5 L5 10 Z" fill="#4d86c9"/></svg>Introduce you to VIP’s + CIP’s</li>
      <li><svg viewBox="0 0 11 10"><path d="M0 0 L6 5 L0 10 Z M5 0 L11 5 L5 10 Z" fill="#4d86c9"/></svg>Jointly design and improve your sales strategy</li>
      <li><svg viewBox="0 0 11 10"><path d="M0 0 L6 5 L0 10 Z M5 0 L11 5 L5 10 Z" fill="#4d86c9"/></svg>Assist you in collection and bed debts</li>
      <li><svg viewBox="0 0 11 10"><path d="M0 0 L6 5 L0 10 Z M5 0 L11 5 L5 10 Z" fill="#4d86c9"/></svg>Train your sales team to increase your closing rate</li>
    </ul>

    <div class="guarantee-tail"></div>
    <svg class="guarantee-fold" width="26" height="14" viewBox="0 0 26 14"><path d="M0 14 L26 0 L26 14 Z" fill="#0f1f3a"/></svg>
    <div class="guarantee">
      <div class="guarantee-inner">
        <div class="guarantee-big">100%</div>
        <div class="guarantee-mid">SATISFACTION<br>GUARANTEED</div>
        <div class="guarantee-small">OR YOUR MONEY BACK</div>
      </div>
    </div>

    <div class="director-photo" role="img" aria-label="Portrait photo of the managing director in a suit"></div>
    <div class="director-name">MARCUS HALE</div>
    <div class="director-role">Managing Director</div>

    <div class="contact">
      <div class="contact-call">CALL US NOW FOR A <strong>FREE CONSULTATION ON</strong></div>
      <div class="contact-phone">04 555 0190</div>
      <div class="contact-address">Located at the Harbor Point Tower, 24th Floor Dubai, UAE<br>Sunday – Thursday: 9:00 am -18:00 pm</div>
      <div class="contact-web">www.nexora.ae</div>
    </div>

    <div class="footer-rule" style="top:733px"></div>
    <div class="footer-band" style="top:736px;height:92px">
      <div class="brand" style="left:57px;top:18px">
        <span class="brand-dot"></span><span class="brand-name">Nexora</span>
      </div>
      <div class="brand-since">SINCE 2004</div>
      <div class="revenue">REVENUE SHARING MODEL<br>If you don’t sell we don’t get paid</div>
    </div>
  </section>

  <section class="flyer flyer--cover">
    <div class="skyline-photo" role="img" aria-label="Dubai city skyline at dusk with the tallest tower and lit buildings under a deep blue sky"></div>
    <div class="footer-rule" style="top:699px"></div>
    <div class="footer-band" style="top:702px;height:90px">
      <div class="brand" style="left:54px;top:27px">
        <span class="brand-dot"></span><span class="brand-name">Nexora</span>
      </div>
      <div class="tagline">YOUR BUSINESS<br>OUR CONNECTIONS</div>
    </div>
  </section>

</main>
</body>
</html>
```